Design a template to be used for multiple product data sheets.

We have currently 10 datasheets for our products we want designed where the information placed in each one should conform to an identical template as far as possible. The datasheets contain both images, text and tables of data. The info. on the sheets should fit the front and back of a USA Letter sized page.

The datasheets must look professional and factual. They are not flyers promoting out products but are presenting factual data on the products and in most cases include Instruction guidelines. So the logo position heading, top introductory text, top image or line drawing would be consistently placed in all sheets as would the footer with our address etc. So we are not looking for a very colourful design but looking for something similar to the brochure as attached produced by Kestrel WB.(Liftmast Installation Guide)

Some color could be used in the footer like a previous data sheet we had designed. (attachment Flomira Deckset Warranty) although would prefer something more subtle.
We have been using Museo Sans font family and would prefer to continue with this.

The copy for the initial sample data sheet is attached. Note that we might make alterations or additions to text and images depending on the design chosen.

So this project is just to provide an initial design for ONE data sheet, front and back which can serve as a template for at least 9 more sheets.
You can refer to our website veltonix .com for further product info.

```html
<!DOCTYPE html>
<html lang="en">
<head>
<meta charset="utf-8">
<title>Veltonix Product Data Sheet</title>
<link href="https://fonts.googleapis.com/css2?family=Mulish:wght@300;400;600;700;800&display=swap" rel="stylesheet">
<style>
  :root{
    --canvas:#e6e6e6;
    --paper:#ffffff;
    --teal:#2b5c65;
    --teal-soft:#5f8990;
    --teal-pale:#dfe9ea;
    --ink:#3a3f42;
    --muted:#7b8286;
    --rule:#c9d0d2;
    --stripe:#eceff0;
    --photo-a:#f1f2f2;
    --photo-b:#d9dcdd;
  }
  *{box-sizing:border-box;margin:0;padding:0}
  html,body{width:1200px;height:900px;overflow:hidden}
  body{background:var(--canvas);font-family:"Mulish",sans-serif;color:var(--ink);position:relative}
  .sheet{position:absolute;top:90px;width:556px;height:720px;background:var(--paper);box-shadow:0 2px 10px rgba(0,0,0,.12);overflow:hidden}
  .sheet--front{left:30px}
  .sheet--back{left:614px}
  .side-band{position:absolute;left:0;top:70px;bottom:0;width:30px;background:linear-gradient(180deg,var(--teal) 0%,var(--teal-soft) 45%,#ffffff 100%)}
  .side-band span{position:absolute;left:50%;top:70px;transform:translateX(-50%) rotate(90deg);transform-origin:center;color:#fff;font-weight:300;font-size:15px;letter-spacing:.5px;white-space:nowrap}
  .brand{position:absolute;left:14px;top:22px;display:flex;align-items:center;gap:8px}
  .brand__mark{width:16px;height:16px;background:var(--teal)}
  .brand__name{font-size:20px;font-weight:300;color:var(--teal-soft);letter-spacing:.4px}
  .photo{position:absolute;background:linear-gradient(160deg,var(--photo-a),var(--photo-b));border-radius:2px}
  .callout{position:absolute;left:240px;width:290px;border:1px solid var(--rule);font-size:7.5px;padding:4px 7px;color:var(--muted);background:#fff}
  .leaders{position:absolute;left:0;top:0}
  h1,h2{color:var(--teal);font-weight:800}
  .title{position:absolute;left:50px;right:26px;font-size:15px;line-height:1.15}
  .body{position:absolute;font-size:7.5px;line-height:1.45;color:var(--ink)}
  .col-head{position:absolute;font-size:9px;font-weight:800;color:var(--teal)}
  .footer{position:absolute;right:26px;bottom:22px;font-size:6.5px;color:var(--muted);text-align:right;line-height:1.7}
  .footer svg{vertical-align:-1px;margin-right:3px}
  .intro-box{position:absolute;left:50px;right:26px;top:76px;border:1px solid var(--rule);padding:6px 8px;font-size:7.5px;line-height:1.45}
  .bullets{position:absolute;font-size:7.5px;line-height:1.7;list-style:none}
  .bullets li::before{content:"";display:inline-block;width:4px;height:4px;background:var(--teal);margin-right:5px;vertical-align:1px}
  .band{position:absolute;left:50px;right:26px;height:16px;background:var(--teal);color:#fff;font-size:9px;font-weight:700;text-align:center;line-height:16px;letter-spacing:.3px}
  .spec{position:absolute;left:50px;right:26px;border-collapse:collapse;font-size:7px}
  .spec td{padding:2px 8px;height:13px}
  .spec tr:nth-child(odd){background:var(--stripe)}
  .spec td:first-child{font-weight:700;color:var(--teal);width:40%}
  .height-box{position:absolute;left:50px;right:26px;border:1px solid var(--rule);display:flex;justify-content:space-around;align-items:flex-end;padding:8px 20px 6px}
  .unit{display:flex;flex-direction:column;align-items:center;gap:4px}
  .unit .thumb{background:linear-gradient(160deg,var(--photo-a),var(--photo-b));border-radius:2px}
  .unit span{font-size:6.5px;font-weight:700;color:var(--ink)}
</style>
</head>
<body>

<section class="sheet sheet--front">
  <div class="brand"><div class="brand__mark"></div><div class="brand__name">Veltonix</div></div>
  <div class="side-band"><span>Veltonix</span></div>

  <div class="photo" role="img" aria-label="Photo of pedestal with wind uplift clips" style="left:55px;top:66px;width:150px;height:150px"></div>
  <svg class="leaders" width="556" height="240" aria-hidden="true">
    <g stroke="#9aa4a7" stroke-width=".7">
      <line x1="180" y1="88" x2="240" y2="80"/>
      <line x1="175" y1="110" x2="240" y2="110"/>
      <line x1="165" y1="150" x2="240" y2="142"/>
      <line x1="190" y1="200" x2="240" y2="180"/>
    </g>
  </svg>
  <div class="callout" style="top:72px">Stainless steel threaded rod locks top to base securely</div>
  <div class="callout" style="top:102px">Uplift clips engage paver edges at each corner joint</div>
  <div class="callout" style="top:134px">Rubber sleeve absorbs vibration and reduces point loads</div>
  <div class="callout" style="top:172px">Wide base plate spreads load on roof membranes</div>

  <h1 class="title" style="top:236px">Wind Uplift Mitigation System for Porcelain Pavers</h1>
  <p class="body" style="left:50px;right:26px;top:258px">This system secures porcelain pavers on raised pedestals against wind uplift on roof terraces. Clips fasten each paver to the pedestal head while the base remains free standing, so the membrane stays intact and the deck can be lifted for access.</p>

  <h2 class="col-head" style="left:50px;top:300px">T2 | 20mm thick porcelain pavers</h2>
  <p class="body" style="left:50px;width:225px;top:314px">Pedestal head fitted with four spring clips. Each clip hooks under the paver edge and is tightened from above with a hex key.</p>
  <div class="photo" role="img" aria-label="Photo of clip on 20mm paver" style="left:50px;top:350px;width:225px;height:150px"></div>

  <h2 class="col-head" style="left:298px;top:300px">T3 | 30mm thick porcelain pavers</h2>
  <p class="body" style="left:298px;width:232px;top:314px">Deeper clips suit thicker tiles. Set the head height first, then lock the clips once all four pavers are level.</p>
  <div class="photo" role="img" aria-label="Photo of clip on 30mm paver" style="left:298px;top:350px;width:232px;height:150px"></div>

  <h1 class="title" style="top:520px">Special Note with Porcelain Paver Installations</h1>
  <p class="body" style="left:50px;right:26px;top:542px">Porcelain pavers are brittle and must be fully supported at every corner. Use a shim where heights differ by more than 2mm, and check the full deck after fixing. Wind zones above 40 m/s need perimeter ballast in addition to clips. Contact our technical team for a site review.</p>

  <div class="footer">
    <div><svg width="7" height="7" viewBox="0 0 10 10"><path d="M5 0C3 0 1.5 1.5 1.5 3.5 1.5 6 5 10 5 10s3.5-4 3.5-6.5C8.5 1.5 7 0 5 0z" fill="#2b5c65"/></svg>Veltonix Inc. · 48 Harbor Lane, Suite 210, Portland, OR 97201</div>
    <div><svg width="7" height="7" viewBox="0 0 10 10"><path d="M2 0l2 2.5-1 1.5c.8 1.5 1.8 2.5 3 3l1.5-1L10 8 8.5 10C4 9.5.5 6 0 1.5z" fill="#2b5c65"/></svg>+1 (503) 555 0147 · info@veltonix.com · veltonix.com</div>
  </div>
</section>

<section class="sheet sheet--back">
  <div class="brand"><div class="brand__mark"></div><div class="brand__name">Veltonix</div></div>
  <div class="side-band"><span>Veltonix</span></div>

  <h1 class="title" style="top:52px">Veltonix ‘Ardent’ Pedestal</h1>
  <p class="intro-box">The Ardent pedestal is a fire rated support for raised decks on roofs and balconies. Its steel body meets non combustible requirements while keeping the fast height adjustment of our standard range.</p>

  <div class="photo" role="img" aria-label="Photo of Ardent steel pedestal" style="left:55px;top:122px;width:110px;height:95px"></div>
  <ul class="bullets" style="left:175px;top:128px">
    <li>Height range 25mm to 600mm</li>
    <li>Load rating 2,000 kg</li>
    <li>Slope correction up to 5%</li>
    <li>Powder coated steel finish</li>
  </ul>
  <ul class="bullets" style="left:360px;top:128px">
    <li>Non combustible to A1 class</li>
    <li>Suits porcelain, stone and timber</li>
    <li>Fits all standard tabs</li>
    <li>Locks with a single turn</li>
  </ul>

  <div class="band" style="top:228px">Specifications &amp; Testing</div>
  <table class="spec" style="top:248px">
    <tr><td>Material</td><td>Powder coated steel</td></tr>
    <tr><td>Fire rating</td><td>Class A1</td></tr>
    <tr><td>Load capacity</td><td>2,000 kg</td></tr>
    <tr><td>Height range</td><td>25–600 mm</td></tr>
    <tr><td>Base diameter</td><td>200 mm</td></tr>
    <tr><td>Head diameter</td><td>150 mm</td></tr>
    <tr><td>Slope correction</td><td>0–5%</td></tr>
    <tr><td>Test standard</td><td>EN 13501-1</td></tr>
  </table>

  <div class="band" style="top:392px">Height Progression</div>
  <div class="height-box" style="top:414px;height:82px">
    <div class="unit"><div class="thumb" role="img" aria-label="Pedestal AP-25" style="width:50px;height:30px"></div><span>AP-25</span></div>
    <div class="unit"><div class="thumb" role="img" aria-label="Pedestal AP-50" style="width:50px;height:40px"></div><span>AP-50</span></div>
    <div class="unit"><div class="thumb" role="img" aria-label="Pedestal AP-75" style="width:50px;height:50px"></div><span>AP-75</span></div>
  </div>
  <div class="height-box" style="top:504px;height:92px">
    <div class="unit"><div class="thumb" role="img" aria-label="Pedestal AP-100" style="width:46px;height:38px"></div><span>AP-100</span></div>
    <div class="unit"><div class="thumb" role="img" aria-label="Pedestal AP-150" style="width:46px;height:48px"></div><span>AP-150</span></div>
    <div class="unit"><div class="thumb" role="img" aria-label="Pedestal AP-225" style="width:46px;height:58px"></div><span>AP-225</span></div>
    <div class="unit"><div class="thumb" role="img" aria-label="Pedestal AP-300" style="width:46px;height:68px"></div><span>AP-300</span></div>
  </div>
  <div class="height-box" style="top:604px;height:72px">
    <div class="unit"><div class="thumb" role="img" aria-label="Pedestal AP-400" style="width:46px;height:34px"></div><span>AP-400</span></div>
    <div class="unit"><div class="thumb" role="img" aria-label="Pedestal AP-500" style="width:46px;height:42px"></div><span>AP-500</span></div>
    <div class="unit"><div class="thumb" role="img" aria-label="Pedestal AP-600" style="width:46px;height:50px"></div><span>AP-600</span></div>
  </div>

  <div class="footer" style="bottom:12px">
    <div><svg width="7" height="7" viewBox="0 0 10 10"><path d="M5 0C3 0 1.5 1.5 1.5 3.5 1.5 6 5 10 5 10s3.5-4 3.5-6.5C8.5 1.5 7 0 5 0z" fill="#2b5c65"/></svg>Veltonix Inc. · 48 Harbor Lane, Suite 210, Portland, OR 97201</div>
    <div><svg width="7" height="7" viewBox="0 0 10 10"><path d="M2 0l2 2.5-1 1.5c.8 1.5 1.8 2.5 3 3l1.5-1L10 8 8.5 10C4 9.5.5 6 0 1.5z" fill="#2b5c65"/></svg>+1 (503) 555 0147 · info@veltonix.com · veltonix.com</div>
  </div>
</section>

</body>
</html>
```